Business Card Design Project

After recently finishing a design project for the company logo using artfoundry, it's now time for a business card. Attached to this is the logo.

The requirements for the business card are pretty straightforward:

- A clean, uncomplicated look
- Consistent usage of fonts
- Designs for both single sided and double sided cards
- A modern layout with preferably space to refer to social media accounts and/or downloadable vcards through a qr code
- consistent application of the company colour scheme: red/white. Hex codes for exact colour can be provided

Thanks!

```html
<!DOCTYPE html>
<html lang="en">
<head>
<meta charset="utf-8">
<title>Kiln Row Staffing – Business Cards</title>
<link href="https://fonts.googleapis.com/css2?family=Oxygen:wght@300;400;700&display=swap" rel="stylesheet">
<style>
  :root {
    --page: #e9e9e9;
    --card-dark: #231f20;
    --card-light: #ffffff;
    --brand-red: #e31e24;
    --ink: #1d1d1b;
    --grey: #8c8c8c;
    --ghost: #eeeeee;
    --ghost-dark: #2c2829;
  }
  * { margin: 0; padding: 0; box-sizing: border-box; }
  html, body { width: 1067px; height: 1200px; overflow: hidden; }
  body {
    background: var(--page);
    font-family: "Oxygen", Arial, sans-serif;
    position: relative;
  }
  .card {
    position: absolute;
    left: 173px;
    width: 720px;
    height: 440px;
    overflow: hidden;
    box-shadow: 0 6px 18px rgba(0,0,0,0.18);
  }
  /* Front */
  .card-front { top: 120px; background: var(--card-dark); }
  .card-front .ghost-pattern {
    position: absolute; left: 0; top: 0; width: 300px; height: 440px;
    background: linear-gradient(90deg, var(--ghost-dark), var(--card-dark));
  }
  .brand { position: absolute; display: flex; align-items: center; }
  .brand-mark { background: var(--brand-red); flex: none; }
  .brand-text { display: flex; flex-direction: column; }
  .brand-name { font-weight: 400; line-height: 1; white-space: nowrap; }
  .brand-tag { font-weight: 400; color: var(--grey); line-height: 1; white-space: nowrap; }

  .card-front .brand { left: 150px; top: 170px; gap: 30px; }
  .card-front .brand-mark { width: 96px; height: 96px; }
  .card-front .brand-name { color: #fff; font-size: 60px; }
  .card-front .brand-tag { font-size: 27px; letter-spacing: 9px; margin-top: 8px; }

  /* Back */
  .card-back { top: 640px; background: var(--card-light); }
  .card-back .ghost-name {
    position: absolute; left: 300px; top: 136px;
    font-size: 84px; font-weight: 700; color: var(--ghost);
    line-height: 1; white-space: nowrap;
  }
  .card-back .ghost-tag {
    position: absolute; left: 304px; top: 222px;
    font-size: 30px; letter-spacing: 12px; color: var(--ghost);
    line-height: 1; white-space: nowrap;
  }
  .card-back .brand { left: 40px; top: 56px; gap: 16px; }
  .card-back .brand-mark { width: 52px; height: 52px; }
  .card-back .brand-name { color: var(--ink); font-size: 38px; font-weight: 700; }
  .card-back .brand-tag { font-size: 19px; letter-spacing: 6px; margin-top: 4px; }

  .contact {
    position: absolute; left: 0; top: 238px;
    display: flex; gap: 22px;
  }
  .contact-bar { width: 14px; height: 150px; background: var(--brand-red); margin-top: 10px; }
  .contact-body { padding-top: 8px; font-size: 13.5px; color: var(--ink); line-height: 1.4; white-space: nowrap; }
  .person-name { font-size: 22px; font-weight: 700; color: var(--brand-red); line-height: 1.2; }
  .person-role { font-size: 13px; margin-bottom: 10px; }
  .label { color: var(--brand-red); }
</style>
</head>
<body>
  <section class="card card-front">
    <div class="ghost-pattern" role="img" aria-label="Faint repeating brand pattern"></div>
    <div class="brand">
      <span class="brand-mark"></span>
      <div class="brand-text">
        <span class="brand-name">Kiln Row</span>
        <span class="brand-tag">STAFFING</span>
      </div>
    </div>
  </section>

  <section class="card card-back">
    <span class="ghost-name">Kiln Row</span>
    <span class="ghost-tag">STAFFING</span>
    <div class="brand">
      <span class="brand-mark"></span>
      <div class="brand-text">
        <span class="brand-name">Kiln Row</span>
        <span class="brand-tag">STAFFING</span>
      </div>
    </div>
    <div class="contact">
      <span class="contact-bar"></span>
      <div class="contact-body">
        <p class="person-name">Sam Porter</p>
        <p class="person-role">Director</p>
        <p>Mill Lane, 47</p>
        <p>310 Clay Road, Westbury NSW 2000 &nbsp;<span class="label">Fax:</span> +61 2 5550 1943</p>
        <p><span class="label">Mob:</span> 0400 182 736 &nbsp;<span class="label">Tel:</span> +61 2 5550 1942 &nbsp;<span class="label">Social:</span> @KilnRowStaff</p>
        <p><span class="label">Page:</span> kilnrow.page/staff &nbsp;<span class="label">Web:</span> www.kilnrowstaff.com</p>
        <p><span class="label">Email:</span> hello@kilnrowstaff.com</p>
      </div>
    </div>
  </section>
</body>
</html>
```